We need a home page that represents us as the best Veterinary Hospital in the State

We need webdesign for a Vet Hospital in Rio de Janeiro, Brazil.
We think the current design is very childish. We want something that looks more like a hospital and not a clinic.
We put a map to guide the content of the sections and also an example of a layout that we don't like but that may serve as a reference as a wireframe.

Target Market(s)

pet owners

Industry/Entity Type

Pet Care

Number of Pages Required

1 page

Requirements
Must have
• Here is a map of the sections and texts we think for home: https://qv.zx/4937018256?t=HpLrTnsKwe
Nice to have
• some sites we like:
https://www.valtoramed.br/Pages/Home.aspx
https://www.mediquiro.com/
Should not have
• This is a design that we started working on and the content is correct. But the layout is poor in detail, bad colors, CTA's without prominence.

https://orlenpixworks.plankview.app/console/share/KT7N2W8RXP/731905246

```html
<!DOCTYPE html>
<html lang="pt-BR">
<head>
<meta charset="utf-8">
<title>Vitta Pet — Hospital Veterinário 24h</title>
<link href="https://fonts.googleapis.com/css2?family=Poppins:wght@400;500;600;700&display=swap" rel="stylesheet">
<style>
:root{
  --blue:#1f6fb5;
  --blue-hero:#2a7fc4;
  --red:#c8173f;
  --pink:#fbe3e8;
  --navy:#1d4670;
  --ink:#1d1d1f;
  --muted:#555;
  --soft:#eef2f6;
  --white:#fff;
}
*{margin:0;padding:0;box-sizing:border-box}
html,body{width:1200px;height:2962px;overflow:hidden}
body{position:relative;font-family:'Poppins',sans-serif;color:var(--ink);background:var(--white)}
.abs{position:absolute}
.topbar{left:0;top:0;width:1200px;height:11px;background:linear-gradient(90deg,var(--red),#7a3a82 50%,var(--blue))}
.header{left:0;top:11px;width:1200px;height:85px;background:var(--white)}
.logo{left:165px;top:24px}
.logo-name{display:flex;align-items:center;gap:8px;font-weight:700;font-size:26px;color:var(--blue);line-height:1}
.logo-dot{width:14px;height:14px;border-radius:50%;background:var(--red)}
.logo-tag{font-size:7.5px;font-weight:600;color:var(--ink);line-height:1.15;margin-top:5px}
.nav{left:390px;top:50px;display:flex;gap:20px;font-size:11px;font-weight:600;text-transform:uppercase;color:var(--ink)}
.hero{left:0;top:96px;width:1200px;height:487px;background:var(--blue-hero)}
.hero-title{left:159px;top:172px;width:470px;font-size:32px;font-weight:600;line-height:1.13;letter-spacing:-.5px;color:var(--white)}
.hero-sub{left:159px;top:300px;width:450px;font-size:17px;line-height:1.3;color:var(--white);font-weight:400}
.hero-btn{left:159px;top:373px;width:207px;height:46px;border:2px solid var(--white);border-radius:4px;color:var(--white);font-size:13px;font-weight:600;display:flex;align-items:center;justify-content:center}
.hero-photo{left:615px;top:121px;width:409px;height:386px;border-radius:200px 200px 0 0;background:linear-gradient(160deg,#e6cbb6,#8b7a6c 60%,#4c4540)}
.services{left:159px;top:507px;width:882px;height:161px;background:var(--white);box-shadow:0 10px 30px rgba(0,0,0,.08);display:flex}
.svc{flex:1;border-right:1px solid #eee;display:flex;flex-direction:column;align-items:center;padding-top:28px}
.svc:last-child{border-right:0}
.svc.active{background:var(--pink);border-bottom:5px solid var(--red)}
.svc-icon{width:72px;height:72px;border-radius:50%;background:var(--red);box-shadow:0 0 0 5px #f6d2da;display:flex;align-items:center;justify-content:center}
.svc-label{margin-top:18px;font-size:15px;font-weight:500}
.h2{left:0;width:1200px;text-align:center;font-size:30px;font-weight:500}
.unit{top:780px;width:281px;height:348px;background:var(--white);box-shadow:0 6px 20px rgba(0,0,0,.08);border-bottom:5px solid var(--blue)}
.unit.red{border-bottom-color:var(--red)}
.unit-img{height:205px;background:linear-gradient(135deg,#4f6b3d,#c9ccc7 55%,#eceeee)}
.unit-body{padding:22px 21px 0}
.unit-title{font-size:15px;font-weight:500}
.unit-addr{margin-top:9px;font-size:11.5px;line-height:1.7;color:var(--ink)}
.unit-link{margin-top:8px;font-size:13px;font-weight:500;color:var(--blue);display:flex;align-items:center;gap:6px}
.unit.red .unit-link{color:var(--red)}
.watermark{left:30px;top:1180px;font-size:118px;font-weight:600;color:#f3f3f4;letter-spacing:-1px;white-space:nowrap}
.band-blue{left:0;top:1386px;width:632px;height:317px;background:var(--blue)}
.band-red{left:632px;top:1386px;width:568px;height:317px;background:var(--red)}
.vet-photo{left:40px;top:1202px;width:420px;height:501px;border-radius:180px 180px 0 0;background:linear-gradient(170deg,#d9b79a,#6b9bd3 45%,#dcdcdc)}
.cat-photo{left:702px;top:1208px;width:253px;height:178px;border-radius:90px;background:linear-gradient(135deg,#8c8c8c,#3c3c3c)}
.watch{left:475px;top:1494px;font-size:23px;font-weight:600;color:var(--white);line-height:.95}
.play{left:593px;top:1499px;width:78px;height:78px;border-radius:50%;background:#1a1a1a;border:2px solid var(--white);display:flex;align-items:center;justify-content:center}
.band-title{left:727px;top:1455px;width:400px;font-size:30px;font-weight:600;line-height:1.12;color:var(--white)}
.band-sub{left:729px;top:1576px;width:270px;font-size:12px;line-height:1.6;color:var(--white)}
.testi{left:0;top:1703px;width:1200px;height:465px;background:var(--soft)}
.avatar{border-radius:50%;background:linear-gradient(135deg,#caa58a,#5a4438)}
.quote-mark{left:190px;top:1862px;font-size:190px;font-weight:700;color:#d8d8d8;line-height:1}
.center-av{left:560px;top:1861px;width:74px;height:74px;border:5px solid var(--white);box-shadow:0 4px 12px rgba(0,0,0,.12)}
.t-name{left:0;top:1952px;width:1200px;text-align:center;font-size:15px;font-weight:500}
.t-text{left:280px;top:1990px;width:640px;text-align:center;font-size:15px;line-height:1.38;color:#333}
.dots{left:574px;top:2100px;display:flex;gap:8px;align-items:center}
.dot{width:9px;height:9px;border-radius:50%;border:1px solid var(--muted)}
.dot.on{width:14px;height:14px;border:2px solid var(--blue);background:radial-gradient(var(--blue) 45%,var(--white) 50%)}
.blog{left:235px;top:2280px;width:730px;height:222px;border:2px solid var(--red);background:var(--white);box-shadow:0 8px 24px rgba(0,0,0,.08);overflow:hidden}
.blog-img{position:absolute;left:3px;top:4px;width:331px;height:211px;background:linear-gradient(120deg,#e7d6c4,#9fb4d6 55%,#f0e8dc)}
.blog-text{position:absolute;left:354px;top:22px;width:360px;display:flex;flex-direction:column}
.blog-title{font-size:25px;font-weight:500;line-height:1.28;letter-spacing:-.4px}
.blog-line{margin-top:12px;width:350px;height:1px;background:#ddd}
.blog-tag{margin-top:14px;padding-left:3px;font-size:14px;font-weight:600}
.blog-corner{position:absolute;right:0;bottom:0;width:0;height:0;border-left:44px solid transparent;border-bottom:36px solid var(--red)}
.blog-arrow{position:absolute;right:6px;bottom:6px}
.cat-peek{left:518px;top:2566px;width:123px;height:57px;border-radius:60px 60px 0 0;background:linear-gradient(180deg,#a1826a,#5c4a3c)}
.footer{left:0;top:2622px;width:1200px;height:340px;background:var(--navy);color:var(--white)}
.f-head{font-size:15px;font-weight:600}
.f-list{font-size:12px;line-height:19px;margin-top:10px;color:#dde6f0}
.f-divider{left:629px;top:2653px;width:1px;height:180px;background:rgba(255,255,255,.35)}
.socials{left:686px;top:2696px;display:flex;gap:12px}
.social{width:30px;height:30px;border-radius:50%;background:var(--white)}
.dog-photo{left:903px;top:2761px;width:138px;height:104px;border-radius:60px 60px 0 0;background:linear-gradient(160deg,#e4c08e,#b6854c)}
.f-rule{left:159px;top:2865px;width:882px;height:1px;background:rgba(255,255,255,.3)}
.f-bottom{left:0;top:2882px;width:1200px;text-align:center;font-size:11.5px;line-height:19px;color:#dde6f0}
</style>
</head>
<body>
<div class="abs topbar"></div>
<header class="abs header"></header>
<div class="abs logo">
  <div class="logo-name"><span>Vitta Pet</span><span class="logo-dot"></span></div>
  <div class="logo-tag">UNIDADE POPULAR<br>ATENDIMENTO AO PET</div>
</div>
<nav class="abs nav">
  <span>Home</span><span>Agendamentos</span><span>Vacinas</span><span>Unidades</span><span>Blog</span><span>Trabalhe Conosco</span><span>A Vitta Pet</span><span>Area do Tutor</span>
</nav>

<section class="abs hero"></section>
<h1 class="abs hero-title">Dedicacao 24h por dia 7 dias por semana pra cuidar de quem voce ama</h1>
<p class="abs hero-sub">Excelentes medicos e infraestrutura completa por um preco que cabe no seu bolso.</p>
<div class="abs hero-btn">Consulte Mais informação</div>
<div class="abs hero-photo" role="img" aria-label="Jovem abraçando um buldogue francês"></div>

<div class="abs services">
  <div class="svc"><div class="svc-icon"><svg width="34" height="34" viewBox="0 0 34 34" fill="none" stroke="#fff" stroke-width="2"><rect x="5" y="6" width="24" height="22" rx="2"/><path d="M5 14h24M17 6v22M10 10h3M21 10h3M9 19h4v5H9zM21 19h4v5h-4z"/></svg></div><div class="svc-label">Pronto-Socorro</div></div>
  <div class="svc"><div class="svc-icon"><svg width="34" height="34" viewBox="0 0 34 34" fill="none" stroke="#fff" stroke-width="2" stroke-linecap="round"><path d="M9 5v8a6 6 0 0 0 12 0V5M15 19v4a6 6 0 0 0 12 0v-3"/><circle cx="27" cy="17" r="3"/></svg></div><div class="svc-label">Consultas</div></div>
  <div class="svc active"><div class="svc-icon"><svg width="34" height="34" viewBox="0 0 34 34" fill="none" stroke="#fff" stroke-width="2"><rect x="4" y="7" width="22" height="20" rx="2"/><path d="M4 13h22M10 4v6M20 4v6M8 17h2M13 17h2M18 17h2M8 21h2M13 21h2"/><circle cx="25" cy="25" r="5" fill="#c8173f"/><path d="M25 22v3l2 1"/></svg></div><div class="svc-label">Agendamentos</div></div>
  <div class="svc"><div class="svc-icon"><svg width="34" height="34" viewBox="0 0 34 34" fill="none" stroke="#fff" stroke-width="2" stroke-linecap="round"><path d="M26 4l4 4M28 6l-5 5M22 8l4 4M24 10L12 22l-4-4L20 6zM10 20l-5 5M6 24l-2 2M13 13l2 2M16 10l2 2"/></svg></div><div class="svc-label">Vacinas</div></div>
  <div class="svc"><div class="svc-icon"><svg width="34" height="34" viewBox="0 0 34 34" fill="none" stroke="#fff" stroke-width="2"><rect x="8" y="5" width="18" height="24" rx="2"/><path d="M5 9v22h16M12 16h10M12 20h10M12 24h7"/><circle cx="17" cy="10" r="2"/></svg></div><div class="svc-label">Resultados</div></div>
</div>

<h2 class="abs h2" style="top:713px">Unidades Vitta Pet</h2>

<article class="abs unit" style="left:160px">
  <div class="unit-img" role="img" aria-label="Fachada da unidade Flamengo"></div>
  <div class="unit-body"><div class="unit-title">Unidade Flamengo</div><div class="unit-addr">Rua das Acácias, 118 Flamengo - Rio de Janeiro/RJ CEP: 22000-118</div><div class="unit-link">Veja no maps <svg width="22" height="10" viewBox="0 0 22 10" fill="none" stroke="currentColor" stroke-width="1.5"><path d="M0 5h20M16 1l4 4-4 4"/></svg></div></div>
</article>
<article class="abs unit red" style="left:462px">
  <div class="unit-img" role="img" aria-label="Fachada da unidade Taquara" style="background:linear-gradient(135deg,#a6b4c6,#7a5a4a 50%,#8a8f8a)"></div>
  <div class="unit-body"><div class="unit-title">Unidade Taquara</div><div class="unit-addr">Rua Serra Alta, 57 Taquara - Rio de Janeiro/RJ CEP: 22700-057</div><div class="unit-link">Veja no maps <svg width="22" height="10" viewBox="0 0 22 10" fill="none" stroke="currentColor" stroke-width="1.5"><path d="M0 5h20M16 1l4 4-4 4"/></svg></div></div>
</article>
<article class="abs unit" style="left:760px">
  <div class="unit-img" role="img" aria-label="Fachada da unidade Copacabana"></div>
  <div class="unit-body"><div class="unit-title">Unidade Copacabana</div><div class="unit-addr">Rua Lagoa Clara, 204 Copacabana - Rio de Janeiro/RJ CEP: 22000-204</div><div class="unit-link">Veja no maps <svg width="22" height="10" viewBox="0 0 22 10" fill="none" stroke="currentColor" stroke-width="1.5"><path d="M0 5h20M16 1l4 4-4 4"/></svg></div></div>
</article>

<div class="abs watermark">UNIDADES VITTA PET</div>
<div class="abs band-blue"></div>
<div class="abs band-red"></div>
<div class="abs cat-photo" role="img" aria-label="Gato malhado caminhando"></div>
<div class="abs vet-photo" role="img" aria-label="Veterinária sorridente com um cão border collie"></div>
<svg class="abs" style="left:500px;top:1450px" width="115" height="50" viewBox="0 0 115 50" fill="none" stroke="#fff" stroke-width="3" stroke-linecap="round"><path d="M8 28C30 0 80 -2 105 38M96 34l9 6 2-11"/></svg>
<div class="abs watch">Watch<br>video</div>
<div class="abs play"><svg width="28" height="30" viewBox="0 0 28 30"><path d="M4 2l22 13L4 28z" fill="#fff"/></svg></div>
<h2 class="abs band-title">Infraestrutura completa e equipe medica disponivel 24h todos os dias</h2>
<p class="abs band-sub">Pronto-socorro, centro de internacao, exames de imagem e cirurgia.</p>

<section class="abs testi"></section>
<h2 class="abs h2" style="top:1762px">O que dizem alguns tutores</h2>
<div class="abs avatar" style="left:221px;top:1793px;width:58px;height:58px" role="img" aria-label="Foto de tutor"></div>
<div class="abs avatar" style="left:911px;top:1818px;width:58px;height:58px" role="img" aria-label="Foto de tutor"></div>
<div class="abs avatar" style="left:-7px;top:1884px;width:64px;height:64px" role="img" aria-label="Foto de tutor"></div>
<div class="abs avatar" style="left:1148px;top:1862px;width:68px;height:68px" role="img" aria-label="Foto de tutora"></div>
<div class="abs avatar" style="left:213px;top:1995px;width:64px;height:64px" role="img" aria-label="Foto de tutor"></div>
<div class="abs avatar" style="left:979px;top:2038px;width:70px;height:70px" role="img" aria-label="Foto de tutora"></div>
<div class="abs quote-mark">“</div>
<svg class="abs" style="left:514px;top:1892px" width="22" height="12" viewBox="0 0 22 12" fill="none" stroke="#333" stroke-width="1.5"><path d="M22 6H2M6 2L2 6l4 4"/></svg>
<svg class="abs" style="left:664px;top:1892px" width="22" height="12" viewBox="0 0 22 12" fill="none" stroke="#333" stroke-width="1.5"><path d="M0 6h20M16 2l4 4-4 4"/></svg>
<div class="abs avatar center-av" role="img" aria-label="Foto de Lia Prado"></div>
<div class="abs t-name">Lia Prado</div>
<p class="abs t-text">"Primeira vez que fui a este local. Levei meu cachorro a uma consulta com o oftalmologista, Dr. Paulo Renz. Profissional excelente! Competente e muito atencioso!!! Foi maravilhoso. Consulta 110 reais. Teve lugares que a consulta com oftalmologista estava 210_290_ quase a meu rim!!!! Fui la e amei"</p>
<div class="abs dots"><span class="dot"></span><span class="dot on"></span><span class="dot"></span></div>

<h2 class="abs h2" style="top:2211px">Voce pode se interessar por</h2>
<article class="abs blog">
  <div class="blog-img" role="img" aria-label="Veterinária examinando um gato com uma menina ao lado"></div>
  <div class="blog-text">
    <h3 class="blog-title">Os perigos da Leishmaniose: quais os sintomas e como prevenir?</h3>
    <div class="blog-line"></div>
    <div class="blog-tag">- Saude. Dica.</div>
  </div>
  <div class="blog-corner"></div>
  <svg class="blog-arrow" width="18" height="10" viewBox="0 0 18 10" fill="none" stroke="#fff" stroke-width="1.5"><path d="M0 5h16M12 1l4 4-4 4"/></svg>
</article>

<div class="abs cat-peek" role="img" aria-label="Gato espiando por cima do rodapé"></div>
<footer class="abs footer"></footer>
<div class="abs" style="left:159px;top:2656px;color:#fff"><div class="f-head">Services</div><div class="f-list">Pronto-Socorro<br>Consultas<br>Exames<br>Vacinas<br>Cirurgias</div></div>
<div class="abs" style="left:308px;top:2656px;color:#fff"><div class="f-head">Vitta Pet</div><div class="f-list">Unidades<br>Blog<br>Trabalhe<br>Conosco<br>Quem<br>Somos</div></div>
<div class="abs" style="left:459px;top:2656px;color:#fff"><div class="f-head">Ajuda</div><div class="f-list">Ouvidoria<br>Fale Conosco</div><div class="f-head" style="margin-top:22px">Tutores</div><div class="f-list">Area do Tutor<br>Agendamentos<br>Resultados de Exames</div></div>
<div class="abs f-divider"></div>
<div class="abs f-head" style="left:686px;top:2657px;color:#fff">Nos acompanhe nas redes sociais</div>
<div class="abs socials"><span class="social" aria-label="Rede social"></span><span class="social" aria-label="Rede social"></span><span class="social" aria-label="Rede social"></span><span class="social" aria-label="Rede social"></span></div>
<div class="abs" style="left:686px;top:2747px;color:#fff"><div class="f-head">Central de Atendimento</div><div class="f-list">+55 21 3000 4100<br>D +55 21 99000-4100</div></div>
<div class="abs dog-photo" role="img" aria-label="Cão labrador olhando para o lado"></div>
<div class="abs f-rule"></div>
<div class="abs f-bottom">Responsavel Tecnico, Dr. Caio Brandt • Medico Veterinario • CRMV-RJ 20517<br>Todos os direitos reservados - Vitta Pet 2021.<br>Desenvolvido por Nortemob</div>
</body>
</html>
```